Mobile Landing Page for giveaway Seedbombs done from a institution for handicaped people

We are a social institution that makes seedbombs that contain wildflowers for bees and other insects. During a sutanibel event, these bombs are given to an audience. On the packaging of the seedbombs, there is a QR code that leads to a landing page. We are producing a video showing how our handicapped clients made the seebombs. The Landigpage should look: sustanible, green, and sozial. On the page, there shoud be this Video, a manual how tho use the seedbombs. Something about our work whith the handicapt people a linkt to our Instagram amd a possibility to get involved whith us as well as a donation button. You can find more information about us on: www.talmatte-kollektiv.ch

Target Market(s)

People that are intressetet in envirement and social impakt

Industry/Entity Type

Social Impakt, Urban Gardening

Coding

Coded - Design and coding required

Number of Pages Required

1 page

Font styles to use
Other font styles liked:
• Joanna

Requirements
Must have
• Be optimised for smartphone
Nice to have
• like a floating page, witch leads you throug the different steps, mabey like a plant with ist growing. From the Bombs to the Plan. Or a little game ore something.

```html
<!DOCTYPE html>
<html lang="en">
<head>
<meta charset="utf-8">
<title>Talmatte – Seedbombs</title>
<link href="https://fonts.googleapis.com/css2?family=Cormorant+Garamond:wght@600;700&family=Poppins:wght@400;500;600&display=swap" rel="stylesheet">
<style>
:root{
  --ink:#1e1e1e;
  --text:#333;
  --green-dark:#2f5d1e;
  --green:#4c8a2b;
  --green-bright:#5fe03a;
  --green-pale:#dff8c8;
  --green-mist:#eefbe4;
  --footer:#1d1d1d;
  --white:#fff;
  --photo-a:#7f9a6a;
  --photo-b:#b7a68a;
}
*{box-sizing:border-box;margin:0;padding:0}
html,body{width:1200px;height:4396px;overflow:hidden}
body{position:relative;background:var(--white);font-family:"Poppins",sans-serif;color:var(--text)}
.abs{position:absolute}
.serif{font-family:"Cormorant Garamond",serif;font-weight:700;color:var(--ink)}
.photo{background:linear-gradient(135deg,var(--photo-a),var(--photo-b))}

/* nav */
.nav{left:0;top:0;width:1200px;height:140px;background:var(--white);z-index:5}
.brand{left:120px;top:42px;font-family:"Cormorant Garamond",serif;font-weight:700;font-size:34px;letter-spacing:3px;color:var(--ink);display:flex;align-items:center;gap:12px}
.brand i{width:14px;height:14px;border-radius:50%;background:var(--green);display:block}
.nav-links{left:405px;top:60px;display:flex;gap:30px;font-size:15px;color:var(--ink);white-space:nowrap}
.nav-links a{color:inherit;text-decoration:none}
.nav-links .active{border-bottom:2px solid var(--ink);padding-bottom:6px}
.nav-donate{left:958px;top:44px;width:150px;height:54px;border:2px solid var(--green-dark);border-radius:27px;display:flex;align-items:center;justify-content:center;font-size:16px;font-weight:500;color:var(--ink);white-space:nowrap}

/* hero */
.hero{left:0;top:140px;width:1200px;height:660px;background:linear-gradient(160deg,#5c7a45,#2e4522 60%,#6f8a56)}
.hero-title{left:0;width:1200px;text-align:center;color:var(--white)}
.hero-kicker{top:258px;font-family:"Poppins",sans-serif;font-size:50px;font-weight:500;letter-spacing:2px}
.hero-name{top:318px;font-family:"Cormorant Garamond",serif;font-weight:700;font-size:84px;letter-spacing:5px}
.play{left:570px;top:445px}
.scroll-pill{left:580px;top:712px;width:40px;height:74px;border-radius:20px;background:#9a9a9a;border:3px solid var(--white)}
.scroll-pill::after{content:"";position:absolute;left:15px;top:18px;width:4px;height:22px;border-radius:2px;background:var(--white)}

h2.serif{font-size:50px;letter-spacing:1px;white-space:nowrap}
.body-text{font-size:17px;line-height:27px;color:var(--text)}
.btn-more{height:58px;width:170px;border:2px solid var(--ink);border-radius:29px;display:flex;align-items:center;padding-left:24px;gap:14px;font-size:16px;color:var(--ink);white-space:nowrap}
.btn-more span{width:34px;height:34px;border-radius:50%;border:2px solid var(--ink);display:flex;align-items:center;justify-content:center;flex:none}

/* steps */
.step-img{width:206px;height:206px;border-radius:50%;border:6px solid var(--white)}
.step-num{width:52px;height:52px;border-radius:50%;background:var(--green-dark);color:var(--white);font-weight:600;font-size:22px;display:flex;align-items:center;justify-content:center;border:3px solid var(--white)}
.step-title{font-size:16px;font-weight:600;color:var(--ink);white-space:nowrap}
.step-text{font-size:14px;line-height:20px;width:262px}
.btn-small{height:38px;width:128px;border:2px solid var(--ink);border-radius:19px;display:flex;align-items:center;padding-left:16px;gap:10px;font-size:13px;color:var(--ink);white-space:nowrap}
.btn-small span{width:20px;height:20px;border-radius:50%;background:var(--ink);display:block;flex:none}

/* instagram */
.insta-card{top:3358px;width:234px;height:244px;border-radius:18px}
.arrow{top:3460px;width:48px;height:48px;border-radius:50%;background:var(--white);box-shadow:0 2px 8px rgba(0,0,0,.25);display:flex;align-items:center;justify-content:center}

/* involve */
.involve{left:176px;top:3738px;width:850px;height:324px;border-radius:28px;background:linear-gradient(160deg,#3d5530,#1f2d18);z-index:2}
.involve-title{left:0;top:52px;width:850px;text-align:center;color:var(--white);font-size:52px;letter-spacing:1px}
.involve-text{left:110px;top:122px;width:630px;text-align:center;color:#e5e5e5;font-size:15px;line-height:22px}
.btn-donate{left:294px;top:210px;width:246px;height:76px;border-radius:38px;background:var(--green-bright);display:flex;align-items:center;justify-content:center;gap:18px;font-weight:600;font-size:20px;color:var(--ink);white-space:nowrap}
.btn-donate span{width:38px;height:38px;border-radius:50%;background:var(--green-dark);display:flex;align-items:center;justify-content:center}

/* footer */
.footer{left:0;top:3940px;width:1200px;height:456px;background:var(--footer)}
.footer-brand{left:90px;top:4130px;font-family:"Cormorant Garamond",serif;font-weight:700;font-size:40px;letter-spacing:4px;color:var(--white)}
.footer-links{left:604px;top:4178px;font-size:16px;color:var(--white);letter-spacing:.5px;white-space:nowrap}
.footer-bar{left:0;top:4268px;width:1200px;height:128px;background:#2a2a2a}
.copy{left:86px;top:4302px;font-size:16px;color:#d0d0d0}
.badge{top:4280px;width:96px;height:96px;border-radius:50%}
.social{top:4296px;width:30px;height:30px;border-radius:50%;border:2px solid #ddd}
</style>
</head>
<body>

<!-- Header -->
<header class="abs nav">
  <div class="abs brand"><i></i>TALMATTE</div>
  <nav class="abs nav-links">
    <a class="active">HOME</a><a>ABOUT US</a><a>HOW TO USE</a><a>OUR WORK</a><a>CONTACT</a>
  </nav>
  <div class="abs nav-donate">DONATE US</div>
</header>

<!-- Hero -->
<section class="abs hero" role="img" aria-label="Video still of people working together in a community garden"></section>
<div class="abs hero-title hero-kicker">WELCOME TO</div>
<div class="abs hero-title hero-name">TALMATTE</div>
<svg class="abs play" width="60" height="44" viewBox="0 0 60 44"><rect width="60" height="44" rx="10" fill="#fff"/><path d="M24 13 L40 22 L24 31Z" fill="#1d1d1d"/></svg>
<svg class="abs" style="left:0;top:560px" width="1200" height="250" viewBox="0 0 1200 250"><path d="M0 80 C200 220 420 200 600 160 C780 120 980 0 1200 60 L1200 250 L0 250Z" fill="#fff"/></svg>
<div class="abs scroll-pill"></div>

<!-- About us -->
<svg class="abs" style="left:40px;top:840px" width="620" height="560" viewBox="0 0 620 560"><path d="M120 40 C260 -10 520 40 580 190 C640 340 560 520 360 540 C180 560 20 470 30 300 C40 160 20 80 120 40Z" fill="#e4f9cf"/></svg>
<div class="abs photo" style="left:72px;top:858px;width:490px;height:490px;border-radius:50%" role="img" aria-label="Photo of two team members standing in the garden under a parasol"></div>
<h2 class="abs serif" style="left:728px;top:950px">ABOUT US</h2>
<p class="abs body-text" style="left:718px;top:1052px;width:400px">Lorem ipsum dolor sit amet, consetghetatur adipi­scing elit, sed do eiusmod tempor incididunt ut labore et dolore magna aliqua. Ut enim ad minim veniam, quis nostrud exercitation ullamco laboris nisi ut</p>
<p class="abs body-text" style="left:718px;top:1200px;width:400px">Aliquip ex ea commodo consequat. Duis aute irure dolor in reprehenderit in voluptate velit esse cillum</p>
<div class="abs btn-more" style="left:718px;top:1300px">Know More <span><svg width="14" height="10" viewBox="0 0 14 10"><path d="M0 5H12M8 1L12 5 8 9" stroke="#1e1e1e" stroke-width="2" fill="none"/></svg></span></div>

<!-- How to use -->
<svg class="abs" style="left:0;top:1420px" width="1200" height="1060" viewBox="0 0 1200 1060"><path d="M0 140 C260 20 520 0 760 90 C950 160 1080 120 1200 60 L1200 900 C1000 1020 780 1060 560 990 C340 920 160 960 0 1010Z" fill="#dff8c8"/></svg>
<h2 class="abs serif" style="left:296px;top:1675px">HOW TO USE THE SEEDBOMBS</h2>

<div class="abs photo step-img" style="left:102px;top:1798px" role="img" aria-label="Child preparing the soil"></div>
<div class="abs step-num" style="left:264px;top:1872px">1</div>
<div class="abs step-title" style="left:342px;top:1834px">PREPARING THE SOIL</div>
<p class="abs body-text step-text" style="left:342px;top:1862px">Lorem ipsum dolor sit amet, consetghctetur adipiscing elit, sed do eiusmod tempor incididunt ut</p>
<div class="abs btn-small" style="left:342px;top:1936px">Read More <span></span></div>

<div class="abs photo step-img" style="left:618px;top:1798px" role="img" aria-label="Person planting seed bombs at a table"></div>
<div class="abs step-num" style="left:780px;top:1872px">2</div>
<div class="abs step-title" style="left:880px;top:1834px">PLANTING SEED BOMBS</div>
<p class="abs body-text step-text" style="left:880px;top:1862px">Lorem ipsum dolor sit amet, consetghctetur adipiscing elit, sed do eiusmod tempor incididunt ut</p>
<div class="abs btn-small" style="left:880px;top:1936px">Read More <span></span></div>

<div class="abs photo step-img" style="left:102px;top:2064px" role="img" aria-label="Watering seed bombs in the soil"></div>
<div class="abs step-num" style="left:264px;top:2140px">3</div>
<div class="abs step-title" style="left:342px;top:2098px">WATERING SEED BOMBS</div>
<p class="abs body-text step-text" style="left:342px;top:2126px">Lorem ipsum dolor sit amet, consetghctetur adipiscing elit, sed do eiusmod tempor incididunt ut</p>
<div class="abs btn-small" style="left:342px;top:2200px">Read More <span></span></div>

<div class="abs step-img" style="left:618px;top:2064px;background:radial-gradient(circle,#4f8a2a,#1c2b14)" role="img" aria-label="Seedling sprouting from the soil"></div>
<div class="abs step-num" style="left:780px;top:2140px">4</div>
<div class="abs step-title" style="left:880px;top:2098px">SPROUTING OF SEED BOMBS</div>
<p class="abs body-text step-text" style="left:880px;top:2126px">Lorem ipsum dolor sit amet, consetghctetur adipiscing elit, sed do eiusmod tempor incididunt ut</p>
<div class="abs btn-small" style="left:880px;top:2200px">Read More <span></span></div>

<!-- About our work -->
<h2 class="abs serif" style="left:88px;top:2568px">ABOUT OUR WORK.</h2>
<p class="abs body-text" style="left:88px;top:2682px;width:420px">Lorem ipsum dolor sit amet, consetghctetur adipi­scing elit, sed do eiusmod tempor incididunt ut labore et dolore magna aliqua. Ut enim ad minim veniam, quis nostrud exercitation ullamco laboris nisi ut</p>
<p class="abs body-text" style="left:88px;top:2848px;width:420px">Aliquip ex ea commodo consequat. Duis aute irure dolor in reprehenderit in voluptate velit esse cillum</p>
<div class="abs btn-more" style="left:88px;top:2932px">Know More <span><svg width="14" height="10" viewBox="0 0 14 10"><path d="M0 5H12M8 1L12 5 8 9" stroke="#1e1e1e" stroke-width="2" fill="none"/></svg></span></div>
<svg class="abs" style="left:560px;top:2520px" width="620" height="620" viewBox="0 0 620 620"><path d="M300 30 C470 20 600 140 560 330 C530 470 600 560 440 590 C280 620 60 560 40 380 C20 200 140 40 300 30Z" fill="#dff8c8"/></svg>
<div class="abs photo" style="left:592px;top:2568px;width:530px;height:530px;border-radius:50%" role="img" aria-label="Photo of a caregiver and a client working together in the workshop"></div>

<!-- Instagram -->
<div class="abs" style="left:0;top:3160px;width:1200px;height:520px;background:var(--green-mist)"></div>
<h2 class="abs serif" style="left:112px;top:3232px">FOLLOW US ON INSTAGRAM</h2>
<div class="abs photo insta-card" style="left:90px" role="img" aria-label="Evening event photo"></div>
<div class="abs photo insta-card" style="left:350px" role="img" aria-label="Clients crafting together"></div>
<div class="abs insta-card" style="left:610px;background:linear-gradient(135deg,#6a6a5a,#3f3f36)" role="img" aria-label="Highlighted post of a workshop table"></div>
<svg class="abs" style="left:680px;top:3440px" width="100" height="50" viewBox="0 0 100 50"><rect x="4" y="8" width="32" height="32" rx="9" fill="none" stroke="#fff" stroke-width="3"/><path d="M70 40 C50 26 54 10 66 12 C70 13 72 16 72 18 C72 16 74 13 78 12 C90 10 94 26 72 40Z" fill="#fff"/></svg>
<div class="abs photo insta-card" style="left:870px" role="img" aria-label="Garden work photo"></div>
<div class="abs arrow" style="left:54px"><svg width="14" height="16" viewBox="0 0 14 16"><path d="M12 1L3 8 12 15" stroke="#333" stroke-width="3" fill="none"/></svg></div>
<div class="abs arrow" style="left:1098px"><svg width="14" height="16" viewBox="0 0 14 16"><path d="M2 1L11 8 2 15" stroke="#333" stroke-width="3" fill="none"/></svg></div>

<!-- Footer band -->
<footer class="abs footer"></footer>

<!-- Get involved -->
<section class="abs involve" role="img" aria-label="Background photo of volunteers in the garden">
  <h2 class="abs serif involve-title" style="color:#fff">GET INVOLVED WHITH US</h2>
  <p class="abs involve-text">Lorem ipsum dolor sit amet, consectetur adipiscing elit. Cras nec luctus gravida tellus consectetur adipiscing. Integer dapibus eleifend magna volutpat interdum.</p>
  <div class="abs btn-donate">DONATE NOW <span><svg width="14" height="10" viewBox="0 0 14 10"><path d="M0 5H12M8 1L12 5 8 9" stroke="#fff" stroke-width="2" fill="none"/></svg></span></div>
</section>

<div class="abs footer-brand">TALMATTE</div>
<div class="abs footer-links">ABOUT US &nbsp;|&nbsp; HOW TO USE &nbsp;|&nbsp; OUR WORK &nbsp;|&nbsp; CONTACT &nbsp;|&nbsp; DONATE US</div>
<div class="abs footer-bar"></div>
<div class="abs copy">Copyright @ 2023 All rights reserved</div>
<div class="abs badge" style="left:470px;background:#8fa6c4"></div>
<div class="abs badge" style="left:578px;background:#c8e7b0"></div>
<div class="abs badge" style="left:686px;background:#e9b8b8"></div>
<div class="abs social" style="left:988px"></div>
<div class="abs social" style="left:1024px"></div>
<div class="abs social" style="left:1060px"></div>
<div class="abs social" style="left:1096px"></div>

</body>
</html>
```